Bref créative
Business Card and Stationary for Hosting Company
Velmor
Professional
Tomas Hadley
General Manager
2815 Quillan Brook Road
Building 5 Suite 410
Marietta, GA 30182
tomash@brimtide.net
www.velmorhostingllc.com
Logo on the back
Please use this logo and let me know if you need anything else.

```html
<!DOCTYPE html>
<html lang="en">
<head>
<meta charset="utf-8">
<title>Velmor Stationery Set</title>
<link rel="stylesheet" href="https://fonts.googleapis.com/css2?family=Montserrat:wght@500;700;800&family=Open+Sans:wght@400;600&display=swap">
<style>
  :root {
    --blue: #1e6cc0;
    --blue-dark: #12509a;
    --orange: #f07a1c;
    --orange-light: #f9a23f;
    --ink: #3a3a3a;
    --muted: #7a7a7a;
    --rule: #d5d8dd;
    --paper: #ffffff;
    --stage: #e9ebee;
  }
  * { box-sizing: border-box; margin: 0; padding: 0; }
  html, body { width: 1200px; height: 785px; overflow: hidden; }
  body { background: var(--stage); font-family: "Open Sans", Arial, sans-serif; color: var(--ink); position: relative; }
  address { font-style: normal; }
  .piece { position: absolute; background: var(--paper); box-shadow: 0 2px 8px rgba(0,0,0,.15); overflow: hidden; }

  /* plain footer band: orange rule over a flat blue strip */
  .footer-band { position: absolute; left: 0; right: 0; bottom: 0; background: var(--blue); border-top: 3px solid var(--orange); display: flex; align-items: center; justify-content: flex-end; padding: 0 16px; }
  .footer-band .web { color: #fff; font-weight: 600; white-space: nowrap; }

  .brand { display: flex; align-items: center; gap: 6px; }
  .brand-dot { border-radius: 50%; background: var(--orange); flex: none; }
  .brand-name { font-family: "Montserrat", Arial, sans-serif; font-weight: 800; color: var(--blue); letter-spacing: .5px; line-height: 1; }
  .tagline { font-family: "Montserrat", Arial, sans-serif; font-weight: 500; color: var(--orange); white-space: nowrap; }

  /* business cards */
  .card { left: 20px; width: 250px; height: 143px; border-radius: 6px; }
  .card-front { top: 30px; }
  .card-front .brand { position: absolute; left: 14px; top: 14px; }
  .card-front .brand-dot { width: 16px; height: 16px; }
  .card-front .brand-name { font-size: 20px; }
  .card-front .tagline { position: absolute; left: 36px; top: 36px; font-size: 5.5px; }
  .card-person { position: absolute; left: 14px; top: 60px; }
  .card-person .name { font-family: "Montserrat", Arial, sans-serif; font-weight: 700; color: var(--blue); font-size: 11px; }
  .card-person .role { font-size: 7px; color: var(--muted); }
  .card-contact { position: absolute; right: 12px; top: 50px; font-size: 6.2px; line-height: 1.55; text-align: right; }
  .card-front .footer-band { height: 12px; }
  .card-back { display: flex; flex-direction: column; align-items: center; justify-content: center; }
  .card-back.blue { top: 200px; background: linear-gradient(135deg, var(--blue) 0%, var(--blue-dark) 100%); }
  .card-back.orange { top: 370px; background: linear-gradient(135deg, var(--orange-light) 0%, var(--orange) 100%); }
  .card-back .brand-dot { width: 22px; height: 22px; background: #fff; }
  .card-back .brand-name { color: #fff; font-size: 26px; }
  .card-back .web { position: absolute; bottom: 12px; right: 14px; color: #fff; font-size: 8px; font-weight: 600; }

  /* letterhead */
  .letterhead { left: 300px; top: 30px; width: 520px; height: 725px; }
  .letterhead .brand { position: absolute; left: 36px; top: 34px; }
  .letterhead .brand-dot { width: 24px; height: 24px; }
  .letterhead .brand-name { font-size: 32px; }
  .letterhead .tagline { position: absolute; left: 66px; top: 68px; font-size: 8px; }
  .sender-address { position: absolute; right: 36px; top: 36px; font-size: 8px; line-height: 1.55; text-align: right; color: var(--muted); }
  .letter-body { position: absolute; left: 36px; right: 44px; top: 130px; font-size: 9.5px; line-height: 1.75; }
  .letter-body p { margin-bottom: 12px; }
  .signature { width: 110px; height: 28px; background: linear-gradient(90deg, #e4e6ea, #f3f4f6); border-radius: 3px; margin: 6px 0 4px; }
  .signer { font-weight: 600; color: var(--blue); }
  .letterhead .footer-band { height: 34px; padding: 0 36px; }
  .letterhead .footer-band .web { font-size: 9px; }

  /* fax sheet */
  .fax { left: 850px; top: 30px; width: 330px; height: 420px; }
  .fax .brand { position: absolute; left: 22px; top: 24px; }
  .fax .brand-dot { width: 16px; height: 16px; }
  .fax .brand-name { font-size: 20px; }
  .fax .sender-address { right: 22px; top: 24px; font-size: 6.5px; }
  .fax-title { position: absolute; right: 22px; top: 74px; font-family: "Montserrat", Arial, sans-serif; font-weight: 700; font-size: 13px; color: var(--blue); }
  .fax-table { position: absolute; left: 22px; top: 100px; width: 286px; border-collapse: collapse; font-size: 7.5px; }
  .fax-table td { border-bottom: 1px solid var(--rule); padding: 6px 0; }
  .fax-table td:first-child { width: 56px; font-weight: 600; color: var(--blue); }
  .fax-notes { position: absolute; left: 22px; right: 22px; top: 290px; height: 60px; border: 1px solid var(--rule); }
  .fax .footer-band { height: 20px; }

  /* envelope */
  .envelope { left: 850px; top: 480px; width: 330px; height: 150px; }
  .envelope .brand { position: absolute; left: 18px; top: 16px; }
  .envelope .brand-dot { width: 14px; height: 14px; }
  .envelope .brand-name { font-size: 18px; }
  .envelope .tagline { position: absolute; left: 38px; top: 36px; font-size: 5px; }
  .envelope .return-address { position: absolute; left: 18px; top: 48px; font-size: 6px; line-height: 1.5; color: var(--muted); }
  .envelope .footer-band { height: 18px; }
  .envelope .footer-band .web { font-size: 7px; }
</style>
</head>
<body>

<!-- Business card front -->
<section class="piece card card-front">
  <div class="brand"><span class="brand-dot"></span><span class="brand-name">VELMOR</span></div>
  <div class="tagline">Your Web Hosting Source</div>
  <div class="card-person">
    <div class="name">Tomas Hadley</div>
    <div class="role">General Manager</div>
  </div>
  <div class="card-contact">
    (770) 555-0142<br>
    tomash@brimtide.net<br>
    www.velmorhostingllc.com<br>
    2815 Quillan Brook Road<br>
    Building 5 Suite 410<br>
    Marietta, GA 30182
  </div>
  <div class="footer-band"></div>
</section>

<!-- Business card backs -->
<section class="piece card card-back blue">
  <div class="brand"><span class="brand-dot"></span><span class="brand-name">VELMOR</span></div>
  <div class="web">www.velmorhostingllc.com</div>
</section>
<section class="piece card card-back orange">
  <div class="brand"><span class="brand-dot"></span><span class="brand-name">VELMOR</span></div>
  <div class="web">www.velmorhostingllc.com</div>
</section>

<!-- Letterhead -->
<section class="piece letterhead">
  <div class="brand"><span class="brand-dot"></span><span class="brand-name">VELMOR</span></div>
  <div class="tagline">Your Web Hosting Source</div>
  <address class="sender-address">
    2815 Quillan Brook Road<br>
    Building 5 Suite 410<br>
    Marietta, GA 30182<br>
    (770) 555-0142
  </address>
  <div class="letter-body">
    <p>Dear Client,</p>
    <p>Thank you for choosing our team to host your websites. We are pleased to confirm that your new hosting plan is now active and fully monitored around the clock by our support engineers.</p>
    <p>Your account includes daily backups, secure email, managed updates and a dedicated contact who will help you plan upgrades as your traffic grows over the coming year.</p>
    <p>Please reach out at any time if you have questions about billing, migration or performance. We look forward to working with you.</p>
    <p>Sincerely,</p>
    <div class="signature" role="img" aria-label="Handwritten signature"></div>
    <div class="signer">Tomas Hadley</div>
    <div>General Manager</div>
  </div>
  <div class="footer-band"><span class="web">www.velmorhostingllc.com</span></div>
</section>

<!-- Fax sheet -->
<section class="piece fax">
  <div class="brand"><span class="brand-dot"></span><span class="brand-name">VELMOR</span></div>
  <address class="sender-address">
    2815 Quillan Brook Road<br>
    Building 5 Suite 410<br>
    Marietta, GA 30182
  </address>
  <div class="fax-title">Fax Sheet</div>
  <table class="fax-table">
    <tr><td>To:</td><td></td></tr>
    <tr><td>From:</td><td></td></tr>
    <tr><td>Company:</td><td></td></tr>
    <tr><td>Fax:</td><td>(770) 555-0143</td></tr>
    <tr><td>Date:</td><td></td></tr>
    <tr><td>Pages:</td><td></td></tr>
  </table>
  <div class="fax-notes"></div>
  <div class="footer-band"></div>
</section>

<!-- Envelope -->
<section class="piece envelope">
  <div class="brand"><span class="brand-dot"></span><span class="brand-name">VELMOR</span></div>
  <div class="tagline">Your Web Hosting Source</div>
  <address class="return-address">
    2815 Quillan Brook Road<br>
    Building 5 Suite 410<br>
    Marietta, GA 30182
  </address>
  <div class="footer-band"><span class="web">www.velmorhostingllc.com</span></div>
</section>
</body>
</html>
```